Brochure Design - Non-Profit Fundraising Stream

We are a non-profit organization that is developing a fundraising project through the donation of life insurance policies. We have three brochures in each English and French that we developed for a sister organization that we want to reintegrate with our Foundation, keeping the same copy text just changing the logos, colors and make it overall more visually appealing. The foundation is called the 'Marrick-Tolle Syndrome Foundation Canada'.
The original files in .docx format are attached as is the full logo and two symbol files. The deliverables would be six documents in total (InDesign or .docx), each brochure in English and French. The color hex codes are:
red: #7b2850
dark blue: #2c79a7
pale blue: #78b2e2

```html
<!DOCTYPE html>
<html lang="en">
<head>
<meta charset="utf-8">
<title>Velmont Charity Services – Flyer</title>
<link rel="stylesheet" href="https://fonts.googleapis.com/css2?family=Tinos:wght@400;700&display=swap">
<style>
  :root {
    --plum: #7b2850;
    --plum-deep: #6a2144;
    --dark-blue: #2c79a7;
    --pale-blue: #78b2e2;
    --pale-tint: #cfe3f4;
    --ink: #2b2b2b;
    --paper: #ffffff;
    --backdrop: #e6e6e6;
    --serif: "Tinos", "Times New Roman", serif;
  }
  * { margin: 0; padding: 0; box-sizing: border-box; }
  html, body { width: 900px; height: 1200px; overflow: hidden; background: var(--backdrop); }
  .flyer {
    position: absolute; left: 30px; top: 6px;
    width: 598px; height: 845px;
    transform: scale(1.4047); transform-origin: 0 0;
    background: linear-gradient(180deg, #ffffff 0%, #fafafa 60%, #e9e9e9 100%);
    font-family: var(--serif); color: var(--ink);
    overflow: hidden;
  }
  .shapes { position: absolute; inset: 0; }
  .abs { position: absolute; }

  .brand-mark { left: 55px; top: 24px; display: flex; align-items: center; gap: 8px;
    color: var(--dark-blue); font-size: 13px; line-height: 1.1; }
  .brand-mark .dot { width: 14px; height: 14px; border-radius: 50%; background: var(--dark-blue); flex: none; }

  .hero-title { left: 300px; width: 298px; top: 78px; text-align: center; color: #fff;
    font-size: 48px; line-height: 45px; letter-spacing: 0.5px; font-weight: 400; }
  .hero-rule { left: 410px; top: 227px; width: 80px; height: 2px; background: #fff; }
  .hero-tagline { left: 300px; width: 298px; top: 250px; text-align: center; color: #fff;
    font-size: 23px; line-height: 24px; }

  .call { left: 0; width: 330px; top: 383px; text-align: center; color: #fff; }
  .call .label { font-size: 22px; line-height: 24px; }
  .call .phone { font-size: 25px; line-height: 28px; letter-spacing: 0.5px; }

  .name-block { left: 25px; top: 500px; }
  .name-block .main { color: var(--dark-blue); font-size: 58px; line-height: 56px; letter-spacing: 1px; }
  .name-block .sub { color: var(--plum); font-size: 25.5px; line-height: 28px; letter-spacing: 0.3px; }

  .benefits { left: 53px; top: 619px; width: 250px; list-style: none; font-size: 9.2px; line-height: 12.6px; }
  .benefits li { height: 44px; }
  .benefits li:nth-child(2) { height: 36px; }
  .benefits li:nth-child(3) { height: 37px; }

  .intro { left: 325px; top: 490px; width: 263px; font-size: 9.3px; line-height: 12.2px;
    text-align: justify; color: #1e1e1e; }

  .policies-head { left: 322px; top: 608px; width: 276px; height: 20px;
    background: var(--plum); border-radius: 10px 0 0 10px; color: #fff;
    font-size: 13px; line-height: 20px; text-align: center; letter-spacing: 0.5px; }
  .policies { left: 330px; top: 642px; list-style: none; font-size: 9.4px; }
  .policies li { display: flex; align-items: center; gap: 12px; height: 30px; }
  .policies .icon { width: 20px; height: 20px; border: 1.2px solid var(--plum);
    border-radius: 50%; display: flex; align-items: center; justify-content: center; background: #fff; }

  .web { left: 62px; top: 820px; color: #fff; font-size: 15px; letter-spacing: 2.5px; }
</style>
</head>
<body>
<div class="flyer">
  <svg class="shapes" viewBox="0 0 598 845" width="598" height="845" aria-hidden="true">
    <defs>
      <linearGradient id="photoTone" x1="0" y1="0" x2="1" y2="1">
        <stop offset="0" stop-color="#f1dccd"/>
        <stop offset="0.5" stop-color="#d9b59c"/>
        <stop offset="1" stop-color="#9fbad6"/>
      </linearGradient>
      <linearGradient id="plumPanel" x1="0" y1="0" x2="0" y2="1">
        <stop offset="0" stop-color="#7b2850"/>
        <stop offset="1" stop-color="#6a2144"/>
      </linearGradient>
    </defs>
    <path d="M300 0 H598 V325 C530 352 430 382 320 380 L300 380 Z" fill="url(#plumPanel)"/>
    <path d="M480 355 C530 342 570 330 598 318 V325 C560 340 520 352 480 360 Z" fill="var(--dark-blue)"/>
    <path d="M320 380 C430 382 530 352 598 325 V372 C545 408 470 420 400 413 C368 409 340 398 320 390 Z" fill="var(--pale-blue)"/>
    <path d="M330 395 C420 420 520 410 598 380 V388 C520 420 430 428 330 400 Z" fill="var(--pale-tint)" opacity="0.8"/>
    <rect x="0" y="78" width="330" height="322" fill="url(#photoTone)" role="img" aria-label="Photo of a smiling family: father, mother, toddler daughter and baby"/>
    <path d="M0 362 C90 340 250 345 335 415 C250 472 90 482 0 468 Z" fill="var(--plum)"/>
    <line x1="33" y1="625" x2="33" y2="742" stroke="var(--plum)" stroke-width="1.2"/>
    <g fill="var(--dark-blue)">
      <circle cx="33" cy="625" r="4.5"/><circle cx="33" cy="669" r="4.5"/>
      <circle cx="33" cy="705" r="4.5"/><circle cx="33" cy="742" r="4.5"/>
    </g>
    <rect x="180" y="795" width="440" height="60" rx="14" fill="var(--pale-blue)"/>
    <path d="M0 812 H330 Q345 812 345 827 V845 H0 Z" fill="var(--plum)"/>
  </svg>

  <div class="abs brand-mark">
    <span class="dot"></span>
    <span>Marrick-Tolle Syndrome<br>Foundation Canada</span>
  </div>

  <h1 class="abs hero-title">VELMONT<br>CHARITY<br>SERVICES</h1>
  <div class="abs hero-rule"></div>
  <p class="abs hero-tagline">Unlock the<br>Hidden value In your<br>life insurance</p>

  <div class="abs call">
    <div class="label">CALL US</div>
    <div class="phone">1 (800) 555-0148</div>
  </div>

  <div class="abs name-block">
    <div class="main">VELMONT</div>
    <div class="sub">CHARITY SERVICES</div>
  </div>

  <ul class="abs benefits">
    <li>You obtain a tax receipt (good for 5 years) for 10%-50% of the face value of the policy (even for term policies that have no “cash surrender value”)</li>
    <li>You convert a “worthless or low cash value policy” into cash in your pocket when you file your income taxes</li>
    <li>Eliminate the burden of annual premium expenses</li>
    <li>A Foundation becomes the owner and beneficiary, and it funds the premiums and collects the benefit upon maturity</li>
  </ul>

  <p class="abs intro">You can maintain or substantially improve your financial position by unlocking the hidden value of your unwanted or unaffordable life insurance via a charitable donation. Every year, seniors over the age of 70 lapse or surrender almost $7 billion of insurance that they might otherwise donate to a charity. You can pay down debt, make major purchases or replenish retirement savings by accessing the value you deserve after paying premiums for decades.</p>

  <div class="abs policies-head">SUITABLE POLICIES</div>
  <ul class="abs policies">
    <li><span class="icon"><svg width="10" height="10" viewBox="0 0 10 10"><path d="M1.5 5.2 L4 7.5 L8.5 2.5" fill="none" stroke="var(--dark-blue)" stroke-width="1.4"/></svg></span>Term, Whole life, Universal or term-to-100 policies</li>
    <li><span class="icon"><svg width="10" height="10" viewBox="0 0 10 10"><path d="M1.5 5.2 L4 7.5 L8.5 2.5" fill="none" stroke="var(--dark-blue)" stroke-width="1.4"/></svg></span>Insured lives over 70 years old</li>
    <li><span class="icon"><svg width="10" height="10" viewBox="0 0 10 10"><path d="M1.5 5.2 L4 7.5 L8.5 2.5" fill="none" stroke="var(--dark-blue)" stroke-width="1.4"/></svg></span>In-force greater than 2 years</li>
    <li><span class="icon"><svg width="10" height="10" viewBox="0 0 10 10"><path d="M1.5 5.2 L4 7.5 L8.5 2.5" fill="none" stroke="var(--dark-blue)" stroke-width="1.4"/></svg></span>Minimum death benefit of $50,000</li>
  </ul>

  <div class="abs web">www.velmont.com</div>
</div>
</body>
</html>
```